E-commerce Website - new look and feel

Link to website
http://198.51.100.64/~vorpanet/vorpanetix_ecommerce/index.php#

Home page
-Header
- -Search bar and add to cart
-Drop down - Multi layer category representation: 1st main category level in menu bar style, 2nd category to follow and 3rd category
-Banner
-Footer

-Search listing

Category page
-Product listing
-

Product detail page
-Product variation tabular view
-

Checkout page
-

404 link/product image not found
Should be fun and engaging customers

Recent search products/ preferred products for customers

all pages:
Headroom js search bar once you are lower down the page

Shrinking navbar

Target Market(s)

Telecommunication installers, electricians working on Industrial plants and projects, on the move customers that need immediate products, procurement officers buying for projects, hard to get items customers, Car hobbyists ( future market ) for some specific product like stainless steel braid(sleeve)

Industry/Entity Type

Telecommunications

Number of Pages Required

5+ page

Colors

Designer to choose colors to be used in the design.

Requirements
Must have
• - less cluttered design
• - Easy to navigate
• - more white area on all pages
• - quick orders
• - repetitive product ordering by customers menu/list
• - branding consistency, logo colours and design
Nice to have
• -modern look
• -user friendly for less technical and computer skilled customers
• -quick to navigate
• - fun text to make customer feel at ease when navigating through website
Should not have
• -too much details
• -

```html
<!DOCTYPE html>
<html lang="en">
<head>
<meta charset="utf-8">
<title>Vorpanetix – Home</title>
<link href="https://fonts.googleapis.com/css2?family=Michroma&family=Lato:wght@400;700&display=swap" rel="stylesheet">
<style>
:root{
  --blue:#0f6cbd;
  --blue-link:#1a86d0;
  --yellow:#f6c600;
  --ink:#111;
  --text:#333;
  --muted:#666;
  --band:#f5f5f5;
  --line:#cfcfcf;
  --white:#fff;
}
*{box-sizing:border-box;margin:0;padding:0}
html,body{width:1200px;height:3267px;overflow:hidden}
body{font-family:"Lato",sans-serif;color:var(--text);background:var(--white);position:relative}
.display{font-family:"Michroma",sans-serif;color:var(--ink);text-transform:uppercase}
a{color:inherit;text-decoration:none}
.abs{position:absolute}

/* top bar */
.topbar{position:absolute;top:0;left:0;width:1200px;height:37px;font-size:13px;color:#444}
.topbar .item{position:absolute;top:10px;display:flex;align-items:center;gap:8px}
.ico-dot{width:18px;height:18px;border-radius:50%;background:var(--yellow);display:flex;align-items:center;justify-content:center}

/* nav */
.navbar{position:absolute;top:37px;left:0;width:1200px;height:61px;background:var(--blue)}
.brand{position:absolute;left:190px;top:13px;display:flex;align-items:center;gap:12px;font-family:"Michroma",sans-serif;font-size:17px;color:var(--white)}
.brand .mark{width:34px;height:34px;border-radius:50%;background:var(--yellow)}
.menu{position:absolute;right:190px;top:22px;display:flex;gap:28px;font-size:13px;color:var(--white);align-items:center}

/* hero */
.hero{position:absolute;top:98px;left:0;width:1200px;height:566px;background:var(--band)}
.hero-title{position:absolute;left:192px;top:218px;width:370px;font-size:22px;line-height:34px;letter-spacing:1px;white-space:nowrap}
.btn{position:absolute;border:2px solid var(--ink);border-radius:3px;background:var(--white);font-size:12px;color:var(--ink);display:flex;align-items:center;justify-content:center}
.hero-media{position:absolute;left:582px;top:142px;width:460px;height:302px;border-radius:50%;background:radial-gradient(ellipse at center,#f5f3d8 0 22%,#c9d83a 23%,#8fbf2a 60%,#d5d84a 100%)}
.arrow{position:absolute;width:30px;height:30px;border-radius:50%}
.arrow.prev{border:2px solid var(--ink);background:var(--white)}
.arrow.next{background:var(--yellow)}
.dots{position:absolute;display:flex;gap:6px}
.dots span{width:7px;height:7px;border-radius:50%;background:var(--ink)}
.dots span.on{background:var(--yellow)}

/* features */
.features{position:absolute;top:664px;left:0;width:1200px;height:164px;background:var(--white)}
.feature{position:absolute;top:33px;width:256px;height:98px;border:2px solid #ddd;display:flex;align-items:center;gap:12px;padding-left:32px}
.feature h4{font-family:"Michroma",sans-serif;font-size:11px;font-weight:400;color:var(--ink)}
.feature p{font-size:11px;color:#555;margin-top:2px}

/* sections */
.section{position:absolute;left:0;width:1200px}
.section-title{position:absolute;left:0;width:1200px;text-align:center;font-size:24px;letter-spacing:1px}
.tabs{position:absolute;top:113px;left:0;width:1200px;display:flex;justify-content:center;gap:24px;font-size:11px;color:#444}
.tabs .on{color:var(--yellow)}

.card{position:absolute;width:194px;height:268px;border:3px solid #d9d9d9;background:var(--white);text-align:center}
.card.active{border:3px solid var(--ink)}
.card .media{margin:14px auto 0;width:150px;height:110px;border-radius:6px}
.card .name{font-family:"Michroma",sans-serif;font-size:10px;color:var(--ink);margin-top:20px;line-height:14px;padding:0 10px}
.card .code{font-size:11px;color:#555;margin-top:14px}
.card .specs{font-size:11px;color:var(--blue-link);margin-top:2px}
.card .price{font-size:12px;color:#555;margin-top:2px}

.about-text{position:absolute;left:279px;top:109px;width:647px;text-align:center;font-size:11px;line-height:15px;color:#444}

.cat{position:absolute;width:193px;height:258px;border:3px solid #d9d9d9;background:var(--white);text-align:center}
.cat .media{margin:22px auto 0;width:150px;height:110px;border-radius:6px}
.cat .name{font-family:"Michroma",sans-serif;font-size:10px;line-height:13px;color:var(--ink);height:44px;margin-top:22px;padding:0 10px;display:flex;align-items:flex-end;justify-content:center}
.cat .link{font-size:11px;color:#333;margin-top:6px}

.photo{position:absolute;left:287px;width:166px;height:166px;border-radius:50%;background:linear-gradient(135deg,#b98d6e,#6a4a3a)}
.stars{color:var(--yellow);font-size:20px;letter-spacing:2px}

.subscribe-input{position:absolute;left:558px;top:28px;width:450px;height:42px;border:2px solid var(--ink);border-radius:21px;background:var(--white);font-size:12px;color:#444;padding-left:24px;display:flex;align-items:center}
.subscribe-input .send{position:absolute;right:-2px;top:-2px;width:74px;height:42px;border:2px solid var(--ink);border-radius:0 21px 21px 0;display:flex;align-items:center;justify-content:center}

/* footer */
.footer{position:absolute;top:2934px;left:0;width:1200px;height:333px;background:var(--blue);color:var(--white)}
.foot-brand{position:absolute;left:190px;top:34px;text-align:center;width:160px}
.foot-brand .mark{width:44px;height:44px;border-radius:50%;background:var(--yellow);margin:0 auto}
.foot-brand .name{font-family:"Michroma",sans-serif;font-size:15px;margin-top:14px}
.foot-col{position:absolute;font-size:11px;line-height:15px}
.foot-col h5{font-family:"Michroma",sans-serif;font-weight:400;font-size:18px;color:var(--yellow);margin-bottom:18px;white-space:nowrap}
.foot-col li{list-style:none;display:flex;gap:10px;margin-bottom:14px}
.bullet{width:6px;height:6px;border-radius:50%;background:var(--yellow);margin-top:4px;flex:none}
.yellow{color:var(--yellow)}
.rule{position:absolute;left:190px;top:257px;width:820px;height:1px;background:rgba(255,255,255,.7)}
</style>
</head>
<body>

<header class="topbar">
  <div class="item" style="left:190px"><span class="ico-dot"><svg width="10" height="10" viewBox="0 0 10 10"><path d="M2 1l2 2-1 1c1 2 2 3 3 3l1-1 2 2-1 1C5 9 1 5 1 2z" fill="#fff"/></svg></span>1300 555 019</div>
  <div class="item" style="left:324px"><span class="ico-dot"><svg width="10" height="8" viewBox="0 0 10 8"><rect x="0.5" y="0.5" width="9" height="7" fill="none" stroke="#fff"/><path d="M1 1l4 3 4-3" fill="none" stroke="#fff"/></svg></span>sales@coralvalecomponents.com.au</div>
  <div class="item" style="left:866px"><span class="ico-dot"><svg width="10" height="10" viewBox="0 0 10 10"><circle cx="5" cy="3" r="2" fill="#fff"/><path d="M1 10c0-3 8-3 8 0z" fill="#fff"/></svg></span>Login</div>
  <div class="item" style="left:944px"><span class="ico-dot"><svg width="10" height="10" viewBox="0 0 10 10"><path d="M0 1h2l1 5h5l1-4H3" fill="none" stroke="#fff"/><circle cx="4" cy="8.5" r="1" fill="#fff"/><circle cx="7.5" cy="8.5" r="1" fill="#fff"/></svg></span>Cart ( 2 )</div>
</header>

<nav class="navbar">
  <a class="brand" href="http://198.51.100.64/~vorpanet/vorpanetix_ecommerce/index.php#"><span class="mark"></span>VORPANETIX</a>
  <div class="menu">
    <span>Home</span><span>Categories ▾</span><span>About Us</span><span>Contact Us</span>
    <svg width="13" height="13" viewBox="0 0 13 13"><circle cx="5.5" cy="5.5" r="4.2" fill="none" stroke="#fff" stroke-width="1.6"/><path d="M8.5 8.5l3.5 3.5" stroke="#fff" stroke-width="1.6"/></svg>
  </div>
</nav>

<section class="hero">
  <svg class="arrow prev" style="left:79px;top:264px" viewBox="0 0 30 30"><path d="M17 9l-6 6 6 6" fill="none" stroke="#111" stroke-width="2.5"/></svg>
  <h1 class="hero-title display" style="font-weight:400">Green / Yellow<br>Earth Cable - Rigid</h1>
  <a class="btn" style="left:192px;top:307px;width:150px;height:37px">Shop Now</a>
  <div class="hero-media" role="img" aria-label="Coil of green and yellow striped earth cable"></div>
  <svg class="arrow next" style="left:1089px;top:264px" viewBox="0 0 30 30"><path d="M13 9l6 6-6 6" fill="none" stroke="#fff" stroke-width="2.5"/></svg>
  <div class="dots" style="left:582px;top:515px"><span class="on"></span><span></span><span></span></div>
</section>

<section class="features">
  <div class="feature" style="left:190px">
    <svg width="30" height="30" viewBox="0 0 30 30"><circle cx="15" cy="13" r="10" fill="none" stroke="#222" stroke-width="2"/><path d="M10 25h10M15 23v4" stroke="#222" stroke-width="2"/></svg>
    <div><h4>FREE SHIPPING</h4><p>Lorem Ipsum is dummy text.</p></div>
  </div>
  <div class="feature" style="left:470px">
    <svg width="30" height="30" viewBox="0 0 30 30"><circle cx="15" cy="15" r="12" fill="none" stroke="#222" stroke-width="2"/><circle cx="15" cy="12" r="4" fill="none" stroke="#222" stroke-width="2"/><path d="M8 23c2-5 12-5 14 0" fill="none" stroke="#222" stroke-width="2"/></svg>
    <div><h4>PREMIUM SUPPORT</h4><p>24/7 Customer service</p></div>
  </div>
  <div class="feature" style="left:749px">
    <svg width="34" height="30" viewBox="0 0 34 30"><rect x="2" y="8" width="18" height="13" fill="none" stroke="#222" stroke-width="2"/><path d="M20 12h7l5 5v4H20" fill="none" stroke="#222" stroke-width="2"/><circle cx="9" cy="23" r="3" fill="#fff" stroke="#222" stroke-width="2"/><circle cx="26" cy="23" r="3" fill="#fff" stroke="#222" stroke-width="2"/></svg>
    <div><h4>PAYMENT METHOD</h4><p>Cash On Delivery</p></div>
  </div>
</section>

<section class="section" style="top:828px;height:566px;background:var(--band)">
  <h2 class="section-title display" style="top:44px;font-weight:400">Feature Products</h2>
  <div class="tabs"><span class="on">ALL</span><span>Newest</span><span>Most Popular</span><span>Other</span></div>
  <svg class="arrow prev" style="left:79px;top:291px" viewBox="0 0 30 30"><path d="M17 9l-6 6 6 6" fill="none" stroke="#111" stroke-width="2.5"/></svg>
  <div class="card" style="left:190px;top:161px">
    <div class="media" role="img" aria-label="Black cold shrink tubes" style="background:linear-gradient(135deg,#555,#111)"></div>
    <div class="name">EPDM COLD SHRINK</div><div class="code">CST-1</div><div class="specs">Specs</div><div class="price">$ 13.95</div>
  </div>
  <div class="card" style="left:396px;top:161px">
    <div class="media" role="img" aria-label="Coil of black flexible conduit" style="background:radial-gradient(circle,#bbb 0 20%,#333 22%,#111 100%)"></div>
    <div class="name">BLACK NYLON FLEXIBLE CONDUIT</div><div class="code" style="margin-top:6px">BNC12</div><div class="specs">Specs</div><div class="price">$ 2.5</div>
  </div>
  <div class="card active" style="left:603px;top:161px">
    <div class="media" role="img" aria-label="Reel of red and blue twin cable" style="width:90px;height:80px;border-radius:50%;background:radial-gradient(circle,#e33 0 30%,#6a3aa8 60%,#2a4ab0 100%)"></div>
    <div class="name" style="margin-top:10px">RED / BLUE<br>DC CABLE - TWIN</div><div class="code" style="margin-top:6px">CAB RB1.5</div><div class="specs">Specs</div><div class="price">$ 1.9</div>
    <svg width="20" height="18" viewBox="0 0 20 18" style="margin-top:6px"><path d="M1 2h3l2 9h10l2-7H5" fill="none" stroke="#111" stroke-width="2"/><circle cx="8" cy="15" r="1.8" fill="#111"/><circle cx="15" cy="15" r="1.8" fill="#111"/></svg>
  </div>
  <div class="card" style="left:812px;top:161px">
    <div class="media" role="img" aria-label="Row of grey circuit breakers" style="background:linear-gradient(180deg,#e8e8e8,#aaa)"></div>
    <div class="name">KESTREL ELECTRIC CIRCUIT BREAKERS</div><div class="code" style="margin-top:6px">SCH10</div><div class="specs">Specs</div><div class="price">$ 12</div>
  </div>
  <svg class="arrow next" style="left:1089px;top:291px" viewBox="0 0 30 30"><path d="M13 9l6 6-6 6" fill="none" stroke="#fff" stroke-width="2.5"/></svg>
  <a class="btn" style="left:522px;top:479px;width:150px;height:37px">View All</a>
</section>

<section class="section" style="top:1394px;height:294px;background:var(--white)">
  <h2 class="section-title display" style="top:64px;font-weight:400">About Vorpanetix</h2>
  <p class="about-text">Lorem Ipsum is simply dummy text of the printing and typesetting industry. Lorem Ipsum has been the industry's standard dummy text ever since the 1500s, when an unknown printer took a galley of type and scrambled it to make a type specimen book. It has survived not only five centuries, but also the leap into electronic typesetting, remaining essentially unchanged. It was popularised in the 1960s with the release of Letraset sheets containing Lorem Ipsum passages, and more recently with desktop publishing software like Aldus PageMaker including versions of Lorem Ipsum.</p>
  <a class="btn" style="left:526px;top:209px;width:150px;height:37px">Read More</a>
</section>

<section class="section" style="top:1688px;height:784px;background:var(--band)">
  <h2 class="section-title display" style="top:48px;font-weight:400">Product Categories</h2>
  <div class="cat" style="left:190px;top:120px"><div class="media" role="img" aria-label="Stainless steel cable ties" style="background:linear-gradient(160deg,#eee,#aaa)"></div><div class="name">STAINLESS STEEL CABLE TIES</div><div class="link">View Category</div></div>
  <div class="cat" style="left:396px;top:120px"><div class="media" role="img" aria-label="Coil of black flexible conduit" style="background:radial-gradient(circle,#bbb 0 20%,#333 22%,#111 100%)"></div><div class="name">BLACK NYLON FLEXIBLE CONDUIT</div><div class="link">View Category</div></div>
  <div class="cat" style="left:603px;top:120px"><div class="media" role="img" aria-label="Bundles of coloured nylon cable ties" style="background:linear-gradient(90deg,#2a4ad0,#e33,#eee,#f6c600,#3a9a3a,#222)"></div><div class="name">NYLON CABLE TIES</div><div class="link">View Category</div></div>
  <div class="cat" style="left:812px;top:120px"><div class="media" role="img" aria-label="Red earth bar insulators" style="background:radial-gradient(circle,#f04a4a,#b81818 60%,#f5f5f5 62%)"></div><div class="name">EARTH BAR INSULATORS</div><div class="link">View Category</div></div>
  <div class="cat" style="left:190px;top:390px"><div class="media" role="img" aria-label="Copper earth bars" style="background:linear-gradient(160deg,#ddd,#999)"></div><div class="name">EARTH BARS</div><div class="link">View Category</div></div>
  <div class="cat" style="left:396px;top:390px"><div class="media" role="img" aria-label="Black cold shrink tubes" style="background:linear-gradient(135deg,#555,#111)"></div><div class="name">EPDM COLD SHRINK</div><div class="link">View Category</div></div>
  <div class="cat" style="left:603px;top:390px"><div class="media" role="img" aria-label="Drum of green and yellow earth cable" style="background:radial-gradient(circle,#222 0 25%,#5aa83a 27%,#2f7a2a 100%)"></div><div class="name">GREEN / YELLOW EARTH CABLE - MULTISTRAND</div><div class="link">View Category</div></div>
  <div class="cat" style="left:812px;top:390px"><div class="media" role="img" aria-label="Yellow fibre patch lead with blue connectors" style="background:radial-gradient(circle,#fff 0 35%,#f0d020 37%,#f6e070 55%,#fff 57%)"></div><div class="name">FIBER PATCH LEADS RUGGEDISED SINGLE MODE DUPLEX</div><div class="link">View Category</div></div>
  <a class="btn" style="left:522px;top:699px;width:155px;height:37px">View All Cateories</a>
</section>

<section class="section" style="top:2472px;height:370px;background:var(--white)">
  <h2 class="section-title display" style="top:60px;font-weight:400">Testimonials</h2>
  <svg class="arrow prev" style="left:76px;top:179px" viewBox="0 0 30 30"><path d="M17 9l-6 6 6 6" fill="none" stroke="#111" stroke-width="2.5"/></svg>
  <div class="photo" style="top:130px" role="img" aria-label="Customer portrait"></div>
  <div class="abs" style="left:470px;top:140px;width:440px">
    <div class="display" style="font-size:17px">Daniel Ashworth</div>
    <div class="stars" style="margin-top:4px">★★★★★</div>
    <p style="font-size:11px;line-height:15px;color:#444;margin-top:6px">Lorem Ipsum is simply dummy text of the printing and typesetting industry. Lorem Ipsum has been the industry's standard dummy text ever since the 1500s.</p>
    <div style="font-size:12px;color:#222;margin-top:8px;display:flex;align-items:center;gap:8px">READ MORE... <svg width="12" height="12" viewBox="0 0 12 12"><circle cx="6" cy="6" r="5" fill="none" stroke="#222"/><path d="M5 3.5l2.5 2.5L5 8.5" fill="none" stroke="#222"/></svg></div>
  </div>
  <svg class="arrow next" style="left:1089px;top:179px" viewBox="0 0 30 30"><path d="M13 9l6 6-6 6" fill="none" stroke="#fff" stroke-width="2.5"/></svg>
  <div class="dots" style="left:576px;top:316px"><span class="on"></span><span></span><span></span></div>
</section>

<section class="section" style="top:2842px;height:92px;background:var(--band)">
  <h2 class="display abs" style="left:190px;top:33px;font-size:24px;font-weight:400">Subscribe Us</h2>
  <div class="subscribe-input">E-Mail Address
    <span class="send"><svg width="22" height="20" viewBox="0 0 22 20"><path d="M1 9L21 1 15 19 10 11z" fill="#111"/><path d="M10 11L21 1" stroke="#fff"/></svg></span>
  </div>
</section>

<footer class="footer">
  <div class="foot-brand"><div class="mark"></div><div class="name">VORPANETIX</div></div>
  <div class="foot-col" style="left:190px;top:130px;width:160px">
    <p>Lorem Ipsum is simply dummy text of the printing and typesetting industry. Lorem Ipsum has been the industry's standard dummy text ever since the 1500s.</p>
    <p class="yellow" style="margin-top:10px;font-size:13px">READ MORE... ⊙</p>
  </div>
  <div class="foot-col" style="left:416px;top:96px">
    <h5>QUICK LINK</h5>
    <ul><li><span class="bullet"></span>Home</li><li><span class="bullet"></span>Categories</li><li><span class="bullet"></span>About Us</li><li><span class="bullet"></span>Contact Us</li></ul>
  </div>
  <div class="foot-col" style="left:610px;top:96px;width:210px">
    <h5>CONTACT US</h5>
    <ul>
      <li><span class="bullet"></span>Victoria : 14 Ember Court, Lyndale, VIC, 3811</li>
      <li><span class="bullet"></span>Queensland: 7b/402 Harlow Rd, Kenmore Flats, QLD, 4070</li>
      <li style="margin-bottom:6px"><span class="bullet"></span>1300 555 019</li>
      <li><span class="bullet"></span>sales@coralvalecomponents.com.au</li>
    </ul>
  </div>
  <div class="foot-col" style="left:838px;top:96px;width:180px">
    <h5>VISIT US</h5>
    <ul><li><span class="bullet"></span>New South Wales : 3/88 Quarry Lane, Belmont Vale, NSW, 2178</li></ul>
  </div>
  <div class="rule"></div>
  <div class="abs" style="left:190px;top:270px;font-size:13px">CopyRight © 2018 Vorpanetix. All Right Reserve</div>
  <div class="abs" style="right:190px;top:270px;font-size:13px">Privacy Policy - Terms &amp; Conditions</div>
</footer>

</body>
</html>
```